Maple Sprout Menu (Vegetarian Restaurant Concept)

Maple Sprout is a new concept fast casual restaurant
renders are attached so you can see the style of restaurant
Maple Sprowt is a vibrant and modern Vegetarian fast casual restaurant concept that mixes fresh food, energy, great décor, and a comfortable, welcoming atmosphere to provide a memorable and all Vegetarian dining experience.
Our Mission is to be top of mind when consumers think Vegetarian food!
Target Market(s)
the menu is vegetarian and appeals to a broad demographic in USA
Colors
Designer to choose colors to be used in the design.
Requirements
Must have
- well colored and well laid out menu - should not be cartoonish
Nice to have
- For Phots please use the shots in this file:
- https://www.filecrate-example.net/sh/kq7trm2wzl4pnad/BBBxT_qPwLdRNVoE_KMS_Tb?dl=0
- note these are untouched and you are free to change as needed
Should not have
- Should not be cartoonish - nor kives, forks etc in the design

```html
<!DOCTYPE html>
<html lang="en">
<head>
<meta charset="utf-8">
<title>Maple Sprout Menu</title>
<link href="https://fonts.googleapis.com/css2?family=Abril+Fatface&family=Roboto+Slab:wght@400;700;900&display=swap" rel="stylesheet">
<style>
  :root {
    --terracotta: #c5703d;
    --charcoal: #25272b;
    --white: #ffffff;
    --accent: #e3803f;
    --rule: #d9d9d9;
  }
  * { margin: 0; padding: 0; box-sizing: border-box; }
  html, body { width: 849px; height: 1200px; overflow: hidden; background: var(--charcoal); }
  .menu {
    position: relative; width: 849px; height: 1200px;
    background: var(--charcoal); overflow: hidden;
    font-family: "Roboto Slab", serif; color: var(--white);
  }
  .side-band {
    position: absolute; left: 0; top: 0; width: 256px; height: 100%;
    background: var(--terracotta);
  }
  .dish-photo {
    position: absolute; border-radius: 50%;
    border: 3px solid rgba(255,255,255,0.85);
  }
  .dish-photo--salad {
    left: 22px; top: 112px; width: 240px; height: 240px;
    background: radial-gradient(circle at 45% 45%, #e7e2c8 0%, #8aa352 35%, #4f6f2c 70%, #8b3a2a 100%);
  }
  .dish-photo--bean {
    left: 22px; top: 474px; width: 240px; height: 240px;
    background: radial-gradient(circle at 50% 50%, #d8c98a 0%, #7e9b3e 40%, #3f2a2c 75%, #5d7a30 100%);
  }
  .dish-photo--bruschetta {
    left: 14px; top: 836px; width: 254px; height: 254px;
    background: radial-gradient(circle at 50% 50%, #e8c067 0%, #d2452e 40%, #7aa03a 70%, #b23a25 100%);
  }
  .menu-title {
    position: absolute; left: 470px; top: 18px;
    font-family: "Abril Fatface", serif; font-size: 58px; letter-spacing: 2px;
    color: var(--white); text-shadow: 3px 3px 0 var(--accent);
  }
  .section-title {
    position: absolute; left: 345px;
    font-weight: 900; font-size: 40px; letter-spacing: 1px; line-height: 1;
  }
  .section-rule {
    position: absolute; left: 345px; width: 470px; height: 2px; background: var(--rule);
  }
  .dish { position: absolute; left: 345px; width: 470px; }
  .dish-name { font-weight: 700; font-size: 25px; line-height: 1.25; }
  .dish-desc {
    margin-top: 4px; font-size: 16px; line-height: 1.4; color: var(--accent);
  }
</style>
</head>
<body>
<main class="menu">
  <div class="side-band"></div>
  <div class="dish-photo dish-photo--salad" role="img" aria-label="Photo of a plated green salad with sliced avocado and toppings"></div>
  <div class="dish-photo dish-photo--bean" role="img" aria-label="Photo of black bean and corn salad in lettuce cups"></div>
  <div class="dish-photo dish-photo--bruschetta" role="img" aria-label="Photo of tomato bruschetta with fresh herbs"></div>

  <h1 class="menu-title">MENU</h1>

  <h2 class="section-title" style="top:188px;">SALADS</h2>
  <div class="section-rule" style="top:236px;"></div>

  <div class="dish" style="top:292px;">
    <div class="dish-name">Brussel Sprout Ceasar</div>
    <p class="dish-desc">little gem romaine, toasted corn bread,<br>parmigiano reggiano</p>
  </div>
  <div class="dish" style="top:395px;">
    <div class="dish-name">Heirloom Beet Salad</div>
    <p class="dish-desc">shaved chioggia beet, roasted golden beet,<br>red quinoa, little gem, arugula, lemon vinaigrette</p>
  </div>
  <div class="dish" style="top:496px;">
    <div class="dish-name">Zesty Black Bean &amp;<br>Corn Salad in Lettuce Cups</div>
    <p class="dish-desc">black beans, avocado and roasted corn topped<br>with feta crumbles in butter lettuce</p>
  </div>
  <div class="dish" style="top:630px;">
    <div class="dish-name">Green, Red and White</div>
    <p class="dish-desc">spring leaves, cherry tomatoes, avocado,<br>roasted almond and goat cheese</p>
  </div>

  <h2 class="section-title" style="top:748px;">TOASTS</h2>
  <div class="section-rule" style="top:796px;"></div>

  <div class="dish" style="top:822px;">
    <div class="dish-name">Everything Avocado Toast</div>
    <p class="dish-desc">avocado on whole grain toast with our<br>signature spice blend</p>
  </div>
  <div class="dish" style="top:930px;">
    <div class="dish-name">Tomato &amp; Beet Bruschetta</div>
  </div>
  <div class="dish" style="top:980px;">
    <div class="dish-name">Vegetable Melt on Garlic Toast</div>
  </div>

  <h2 class="section-title" style="top:1060px;">Soup</h2>
  <div class="section-rule" style="top:1108px;"></div>

  <div class="dish" style="top:1138px;">
    <div class="dish-name">Black Bean Chowder</div>
  </div>
</main>
</body>
</html>
```